Morrow Realty Marketing Brochure

We are looking for a refresh/modern design to use on our marketing brochures...the blue paint brush stroke takes up a lot of space and isn't really speaking to us. Most of the material does not need to be reproduced...we are just looking for a clean template that we can use on all of our brochure pages, and then would like help on page 11 to make these pages look more professional.
Target Market(s)
Real Estate Developers, Small Businesses looking to lease space
Industry/Entity Type
Real Estate Development
Requirements
Nice to have
- Colors complementing the Morrow Logo

```html
<!DOCTYPE html>
<html lang="en">
<head>
<meta charset="utf-8">
<title>Morrow Realty Brochure Pages</title>
<link href="https://fonts.googleapis.com/css2?family=Open+Sans:wght@400;600;700&display=swap" rel="stylesheet">
<style>
:root{
  --brand:#1560d8;
  --brand-dark:#0f4fb8;
  --brand-soft:#8fb4ee;
  --brand-pale:#dce8fa;
  --paper:#ffffff;
  --stage:#ffffff;
  --ink-muted:#7c96c4;
  --map-land:#cdd9d8;
  --map-lake:#8da3a8;
  --plan:#d3dbe6;
}
*{margin:0;padding:0;box-sizing:border-box}
html,body{width:1200px;height:652px;overflow:hidden;background:var(--stage)}
body{font-family:"Open Sans",sans-serif;position:relative}
.page{position:absolute;width:364px;height:281px;overflow:hidden;box-shadow:2px 3px 8px rgba(0,0,0,.18)}
.blue{background:var(--brand);color:#fff}
.white{background:var(--paper);color:var(--brand)}
.abs{position:absolute;white-space:nowrap}
.brand{display:flex;align-items:center;gap:4px;font-weight:600;font-size:11px;letter-spacing:.3px;color:#fff}
.brand .mark{width:9px;height:9px;background:#fff}
.hint{font-size:3.4px;letter-spacing:.8px;color:rgba(255,255,255,.55);text-align:center}
.white .hint{color:#b7c3d6}
.num{font-weight:400;line-height:1}
.bar{position:absolute;width:1px;background:currentColor}
.pageno{font-size:3.6px;font-weight:600}
.line{position:absolute;height:1px;background:currentColor}
.dot{position:absolute;width:2.6px;height:2.6px;border-radius:50%;background:currentColor;top:-1px}
.panel{position:absolute;left:0;top:0;width:118px;height:281px;background:var(--brand)}
.perk{position:absolute;font-size:6.6px;font-weight:600}
.perk::before{content:"";position:absolute;left:-12px;top:2px;width:5px;height:5px;background:currentColor;border-radius:1px}
.perk.light{color:var(--brand-soft)}
.perk svg{position:absolute;left:4px;top:11px}
.agent{position:absolute;top:75px;width:75px}
.agent .photo{width:75px;height:75px;background:linear-gradient(160deg,#8a7a6a,#4a5a78)}
.agent .name{font-size:5.8px;font-weight:600;margin-top:10px}
.agent .info{font-size:3.8px;margin-top:3px;line-height:1.9}
</style>
</head>
<body>

<!-- Cover -->
<section class="page blue" style="left:26px;top:31px">
  <div class="abs" style="left:149px;top:22px;height:236px;border-left:1px dashed rgba(20,40,90,.6)"></div>
  <div class="line" style="left:91px;top:107px;width:224px;color:rgba(20,40,90,.55)"></div>
  <div class="abs brand" style="left:149px;top:66px"><span class="mark"></span>MORROW REALTY</div>
  <div class="abs hint" style="left:170px;top:101px;background:var(--brand);padding:0 3px">proposed project name and address<br>(centralised)</div>
  <div class="abs num" style="left:97px;top:121px;font-size:28px">28</div>
  <div class="bar" style="left:138px;top:116px;height:36px;background:#fff"></div>
  <div class="abs" style="left:149px;top:120px;font-size:14px">North Alder</div>
  <div class="abs" style="left:149px;top:140px;font-size:6px">28 North Alder Avenue Brookfield Heights, IL 60100</div>
  <div class="abs" style="left:149px;top:157px;font-size:12px;line-height:1.2">Renovations Planned<br>(2021)</div>
</section>

<!-- Page 01 -->
<section class="page white" style="left:418px;top:31px">
  <div class="panel"></div>
  <div class="abs brand" style="left:23px;top:24px"><span class="mark"></span>MORROW</div>
  <div class="abs" style="left:24px;top:128px;width:15px;height:1px;background:#fff"></div>
  <div class="abs num" style="left:44px;top:120px;font-size:16px;color:#fff">57,856</div>
  <div class="abs" style="left:44px;top:139px;font-size:5.5px;color:#fff">Gross Square Feet</div>
  <div class="abs" style="left:24px;top:169px;width:15px;height:1px;background:#fff"></div>
  <div class="abs num" style="left:44px;top:161px;font-size:16px;color:#fff">19,222</div>
  <div class="abs" style="left:44px;top:180px;font-size:5.5px;color:#fff">SF Floorplates</div>
  <div class="abs hint" style="left:80px;top:150px;transform:rotate(-90deg);transform-origin:left top">proposed project size and date</div>
  <div class="abs pageno" style="left:80px;top:254px;color:#fff">page 01</div>

  <div class="line" style="left:124px;top:11px;width:232px;color:#dde3ec"></div>
  <div class="abs hint" style="left:192px;top:9px;background:#fff;padding:0 3px">proposed project name and address<br>(centralised - template 1)</div>
  <div class="abs num" style="left:163px;top:24px;font-size:22px">28</div>
  <div class="bar" style="left:198px;top:20px;height:30px;color:var(--brand)"></div>
  <div class="abs" style="left:208px;top:23px;font-size:11px">North Alder</div>
  <div class="abs" style="left:208px;top:38px;font-size:4.8px">28 North Alder Avenue Brookfield Heights, IL 60100</div>
  <div class="line" style="left:208px;top:66px;width:148px;color:#dde3ec"></div>
  <div class="abs hint" style="left:208px;top:64px;background:#fff;padding-right:3px">proposed project title right below address</div>
  <div class="abs" style="left:208px;top:71px;font-size:10px;line-height:1.2">Renovations Planned<br>(2021)</div>
  <div class="abs" role="img" aria-label="Rendering of a two-storey brick corner building with black awnings on a street with pedestrians" style="left:118px;top:110px;width:246px;height:171px;background:linear-gradient(180deg,#7fd0e0 0%,#a9ddd8 40%,#8c5a4a 55%,#6d5a4e 78%,#b7b2ac 100%)"></div>
</section>

<!-- Page 02 -->
<section class="page white" style="left:810px;top:31px">
  <div class="panel"></div>
  <div class="abs brand" style="left:23px;top:24px"><span class="mark"></span>MORROW</div>
  <div class="abs hint" style="left:17px;top:105px">proposed project name and address<br>(template 2)</div>
  <div class="abs num" style="left:23px;top:120px;font-size:20px;color:#fff">28</div>
  <div class="abs" style="left:23px;top:141px;font-size:11px;color:#fff">North Alder</div>
  <div class="abs" style="left:23px;top:156px;font-size:4.6px;line-height:1.45;color:#fff">28 North Alder Avenue<br>Brookfield Heights,<br>IL 60100</div>
  <div class="abs hint" style="left:26px;top:184px">proposed project title right<br>below address</div>
  <div class="abs" style="left:23px;top:194px;font-size:8.5px;line-height:1.25;color:#fff">Renovations Planned<br>(2021)</div>
  <div class="abs pageno" style="left:80px;top:254px;color:#fff">page 02</div>
  <div class="abs" role="img" aria-label="Regional road map of the metro area and lakeshore with highway markers" style="left:118px;top:0;width:246px;height:281px;background:linear-gradient(90deg,var(--map-land) 0%,var(--map-land) 68%,var(--map-lake) 76%,var(--map-lake) 100%)"></div>
  <div class="abs" style="left:139px;top:23px;font-size:14px">Regional Map</div>
  <div class="abs" style="left:205px;top:88px;background:var(--brand);color:#fff;font-size:8px;font-weight:700;padding:2px 5px;border-radius:2px">SITE</div>
  <svg class="abs" style="left:220px;top:101px" width="18" height="14"><path d="M2 0 L16 12 L10 0Z" fill="var(--brand)"/></svg>
</section>

<!-- Page 08 -->
<section class="page white" style="left:26px;top:340px">
  <div class="abs" style="left:23px;top:24px;width:6px;height:6px;background:var(--brand-soft);border-radius:1px"></div>
  <div class="abs" style="left:36px;top:23px;font-size:7px;font-weight:600;line-height:1.35;color:var(--brand-soft)">PENDING<br>LEASE</div>
  <div class="abs" style="left:23px;top:54px;width:6px;height:6px;background:var(--brand);border-radius:1px"></div>
  <div class="abs" style="left:36px;top:53px;font-size:7px;font-weight:600">LEASED</div>
  <div class="abs" style="left:23px;top:153px;font-size:8.5px;line-height:1.25">Renovations Planned<br>(2021)</div>
  <div class="abs" role="img" aria-label="Second floor architectural plan with leased suites shaded blue" style="left:114px;top:12px;width:228px;height:168px;background:linear-gradient(180deg,var(--plan) 0%,var(--plan) 55%,#7ea6e4 60%,#6e98df 100%)"></div>
  <div class="abs" style="left:0;top:187px;width:364px;height:94px;background:var(--brand)"></div>
  <div class="abs brand" style="left:23px;top:207px"><span class="mark"></span>MORROW</div>
  <div class="line" style="left:140px;top:200px;width:145px;color:rgba(20,40,90,.55)"></div>
  <div class="abs hint" style="left:140px;top:198px;background:var(--brand);padding-right:3px">proposed subtitle</div>
  <div class="abs" style="left:139px;top:204px;font-size:14px;color:#fff">Second Floor Floorplan</div>
  <div class="bar" style="left:140px;top:223px;height:11px;background:#fff"></div>
  <div class="abs" style="left:145px;top:225px;font-size:5.6px;color:#fff">19,222 SF Floorplate Suites From 1,338 SF</div>
  <div class="line" style="left:140px;top:242px;width:145px;color:rgba(20,40,90,.55)"></div>
  <div class="abs hint" style="left:140px;top:240px;background:var(--brand);padding-right:3px">proposed subtitle content</div>
  <div class="abs pageno" style="left:327px;top:255px;color:#fff">page 08</div>
</section>

<!-- Page 11 -->
<section class="page white" style="left:418px;top:340px">
  <div class="abs" style="left:0;top:0;width:364px;height:93px;background:var(--brand)"></div>
  <div class="abs brand" style="left:23px;top:25px"><span class="mark"></span>MORROW</div>
  <div class="line" style="left:140px;top:18px;width:138px;color:rgba(20,40,90,.55)"></div>
  <div class="abs hint" style="left:140px;top:16px;background:var(--brand);padding-right:3px">proposed subtitle</div>
  <div class="abs" style="left:139px;top:23px;font-size:14px;color:#fff">Location Perks</div>
  <div class="bar" style="left:140px;top:42px;height:11px;background:#fff"></div>
  <div class="abs" style="left:145px;top:44px;font-size:5.6px;color:#fff">Facilities and Services available</div>
  <div class="line" style="left:140px;top:60px;width:138px;color:rgba(20,40,90,.55)"></div>
  <div class="abs hint" style="left:140px;top:58px;background:var(--brand);padding-right:3px">proposed subtitle content</div>
  <div class="abs" style="left:23px;top:195px;font-size:8.5px;line-height:1.25">Renovations Planned<br>(2021)</div>

  <div class="perk light" style="left:153px;top:112px">Wheelchair Accessible
    <svg width="12" height="12" viewBox="0 0 12 12" fill="none" stroke="currentColor" stroke-width="1.1" style="color:var(--brand)"><circle cx="6" cy="1.6" r="1.1" fill="currentColor" stroke="none"/><path d="M5.5 3.5v3.5h3l1 3"/><path d="M4 5.5a3 3 0 1 0 4 4"/></svg></div>
  <div class="perk" style="left:262px;top:112px">Hi-Speed Wi-Fi
    <svg width="12" height="12" viewBox="0 0 12 12" fill="none" stroke="currentColor" stroke-width="1.1"><path d="M1 5a7 7 0 0 1 10 0"/><path d="M3 7a4 4 0 0 1 6 0"/><circle cx="6" cy="9.3" r=".9" fill="currentColor"/></svg></div>
  <div class="perk" style="left:153px;top:147px">Community Manager
    <svg width="16" height="12" viewBox="0 0 16 12" fill="currentColor"><circle cx="8" cy="3" r="1.8"/><path d="M5 11a3 3 0 0 1 6 0z"/><circle cx="3" cy="4.5" r="1.4"/><path d="M0.5 11a2.5 2.5 0 0 1 5 0z"/><circle cx="13" cy="4.5" r="1.4"/><path d="M10.5 11a2.5 2.5 0 0 1 5 0z"/></svg></div>
  <div class="perk light" style="left:262px;top:147px">Conference Rooms
    <svg width="16" height="12" viewBox="0 0 16 12" fill="currentColor" style="color:var(--brand)"><circle cx="4" cy="3" r="1.4"/><circle cx="8" cy="2.5" r="1.4"/><circle cx="12" cy="3" r="1.4"/><path d="M1 8a3 3 0 0 1 14 0z"/><rect x="0" y="9" width="16" height="2"/></svg></div>
  <div class="perk light" style="left:153px;top:182px">Bike Room &amp; Showers
    <svg width="14" height="12" viewBox="0 0 14 12" fill="none" stroke="currentColor" stroke-width="1" style="color:var(--brand)"><circle cx="3" cy="8.5" r="2.5"/><circle cx="11" cy="8.5" r="2.5"/><path d="M3 8.5l3-4h3l2 4M6 4.5l1.5 4"/><circle cx="8" cy="1.5" r="1" fill="currentColor" stroke="none"/></svg></div>
  <div class="perk" style="left:262px;top:182px">Flexible Contracts
    <svg width="12" height="13" viewBox="0 0 12 13" fill="none" stroke="currentColor" stroke-width="1"><rect x="1.5" y=".5" width="9" height="12"/><path d="M3.5 3.5h5M3.5 5.5h5M3.5 7.5h5M3.5 10h2"/></svg></div>
  <div class="perk" style="left:153px;top:217px">Coworking
    <svg width="16" height="12" viewBox="0 0 16 12" fill="currentColor"><circle cx="3.5" cy="2.5" r="1.4"/><circle cx="12.5" cy="2.5" r="1.4"/><rect x="2" y="4.5" width="3" height="4"/><rect x="11" y="4.5" width="3" height="4"/><rect x="0" y="7" width="16" height="1.2"/><rect x="3" y="8" width="1" height="4"/><rect x="12" y="8" width="1" height="4"/></svg></div>
  <div class="perk light" style="left:262px;top:217px">Tenant Amenities
    <svg width="13" height="13" viewBox="0 0 13 13" fill="currentColor" style="color:var(--brand)"><rect x="1" y="4" width="8" height="8" rx="1"/><path d="M9 6h1.5a1.8 1.8 0 0 1 0 3.6H9v-1h1.5a.8.8 0 0 0 0-1.6H9z"/><path d="M4 0.5v2.5M6 0.5v2.5" stroke="currentColor" stroke-width=".7"/></svg></div>
  <div class="abs pageno" style="left:328px;top:255px">page 11</div>
</section>

<!-- Contacts -->
<section class="page blue" style="left:810px;top:340px">
  <div class="abs num" style="left:90px;top:22px;font-size:28px">28</div>
  <div class="bar" style="left:132px;top:18px;height:37px;background:#fff"></div>
  <div class="abs" style="left:142px;top:23px;font-size:14px">North Alder</div>
  <div class="abs" style="left:142px;top:42px;font-size:6px">28 North Alder Avenue Brookfield Heights, IL 60100</div>

  <div class="agent" style="left:53px">
    <div class="photo" role="img" aria-label="Portrait photo of agent Owen Hallbrook"></div>
    <div class="name">Owen Hallbrook</div>
    <div class="info">T : 555-310-2241<br>E : ohallbrook@morrowrealty.com</div>
  </div>
  <div class="agent" style="left:145px">
    <div class="photo" role="img" aria-label="Portrait photo of agent Clara Dunmore"></div>
    <div class="name">Clara Dunmore</div>
    <div class="info">T : 555-418-7730<br>E : cdunmore@morrowrealty.com</div>
  </div>
  <div class="agent" style="left:237px">
    <div class="photo" role="img" aria-label="Portrait photo of agent Miles Ardent"></div>
    <div class="name">Miles Ardent</div>
    <div class="info">T : 555-206-9184<br>E : mardent@morrowrealty.com</div>
  </div>

  <div class="abs brand" style="left:146px;top:209px"><span class="mark"></span>MORROW</div>
  <div class="abs" style="left:0;width:364px;top:249px;font-size:3.3px;line-height:1.5;text-align:center;color:rgba(255,255,255,.9)">©2021 Morrow Realty, LLC. All rights reserved. All information contained herein is from sources deemed reliable; however,<br>no representation or warranty is made to the accuracy thereof.</div>
</section>

</body>
</html>
```